Balloon and backdrop van design PINK AND GREEN MOUNTAIN VIDBES

I’m looking for a bold, eye-catching wrap design for a Trekvale van for my event décor company Bash by the Creek in Asheville, NC.
Style:
Beverly Hills–inspired with a mountain twist. Think playful luxury, glamorous, fun, and very Instagram-worthy.
Colors:
The wrap should be very pink, with pink and forest green as the main colors.
Graphics:
Please incorporate:
Blue Ridge–style mountains
North Carolina pine trees
Optional subtle celebratory elements if they fit the design
Logo & Copy (sides and back of van):
Bash by the Creek
Decor That Dazzles!
bashbythecreekzq.example
Custom event decor, balloons, backdrops, and event planning
The logo should be prominent on the sides and back, and the text should be easy to read from a distance.
I am attaching an AI concept I love for inspiration.
Please provide:
A full wrap option
A half wrap option
Target Market(s)
Luxury clients and business owners
Industry/Entity Type
Party and Events
Look and feel
Each slider illustrates characteristics of the customer's brand and the style your logo design should communicate.

```html
<!DOCTYPE html>
<html lang="en">
<head>
<meta charset="utf-8">
<title>Bash by the Creek – Rear Door Wrap</title>
<link href="https://fonts.googleapis.com/css2?family=Bitter:wght@500;700&family=Lobster&display=swap" rel="stylesheet">
<style>
  :root{
    --canvas:#cccccc;
    --pink:#f06d92;
    --pink-deep:#e0436a;
    --teal:#1d6b6b;
    --forest:#4f7a44;
    --forest-dark:#2f5230;
    --mist:#e9e2ea;
    --blush:#ecd6e2;
    --white:#ffffff;
  }
  *{margin:0;padding:0;box-sizing:border-box}
  html,body{width:1200px;height:1001px;overflow:hidden;background:var(--canvas)}
  .wrap-panel{
    position:absolute;left:175px;top:50px;width:850px;height:900px;
    overflow:hidden;border-radius:6px;
  }
  .scenery{
    position:absolute;inset:0;
    background:
      radial-gradient(ellipse at 80% 75%, rgba(240,236,240,.85) 0%, rgba(240,236,240,0) 45%),
      linear-gradient(180deg, var(--mist) 0%, var(--blush) 22%, #a9b59a 45%, var(--forest) 65%, var(--forest-dark) 100%);
  }
  .brand{
    position:absolute;left:0;right:0;top:120px;
    display:flex;align-items:center;justify-content:center;gap:22px;
  }
  .brand-dot{width:58px;height:58px;border-radius:50%;background:var(--pink-deep);flex:none}
  .brand-name{
    font-family:"Bitter",serif;font-weight:700;font-size:78px;color:var(--teal);
    letter-spacing:-1px;line-height:1;
  }
  .tagline{
    position:absolute;left:0;right:0;top:330px;text-align:center;
    font-family:"Lobster",cursive;font-size:66px;color:var(--pink-deep);
    text-shadow:2px 2px 0 var(--white),-2px -2px 0 var(--white),2px -2px 0 var(--white),-2px 2px 0 var(--white),4px 5px 0 rgba(90,20,40,.5);
  }
  .contact{
    position:absolute;top:462px;left:0;right:0;
    display:flex;justify-content:center;gap:12px;
  }
  .pill{
    height:48px;border-radius:24px;display:flex;align-items:center;gap:10px;
    padding:0 22px;color:var(--white);font-family:"Bitter",serif;font-weight:500;font-size:28px;white-space:nowrap;
  }
  .pill svg{width:22px;height:22px;flex:none}
  .pill-phone{background:var(--pink-deep)}
  .pill-web{background:var(--teal);font-size:26px}
  .services{
    position:absolute;left:50px;top:530px;list-style:none;
    font-family:"Bitter",serif;font-weight:500;font-size:34px;color:var(--white);line-height:41px;
    text-shadow:1px 2px 3px rgba(0,0,0,.75);
  }
  .services li{display:flex;align-items:center;gap:8px}
  .services svg{width:24px;height:24px;flex:none}
</style>
</head>
<body>
  <main class="wrap-panel">
    <div class="scenery" role="img" aria-label="Misty forested Blue Ridge mountain landscape with pink-tinted sky and rolling clouds"></div>

    <div class="brand">
      <span class="brand-dot"></span>
      <span class="brand-name">Bash by the Creek</span>
    </div>

    <div class="tagline">Decor That Dazzles</div>

    <div class="contact">
      <div class="pill pill-phone">
        <svg viewBox="0 0 24 24"><path fill="#fff" d="M6.6 10.8a15.1 15.1 0 0 0 6.6 6.6l2.2-2.2a1 1 0 0 1 1-.25 11.4 11.4 0 0 0 3.6.57 1 1 0 0 1 1 1V20a1 1 0 0 1-1 1A17 17 0 0 1 3 4a1 1 0 0 1 1-1h3.5a1 1 0 0 1 1 1c0 1.25.2 2.450.57 3.6a1 1 0 0 1-.25 1z"/></svg>
        (555) 014-2287
      </div>
      <div class="pill pill-web">
        <svg viewBox="0 0 24 24" fill="none" stroke="#fff" stroke-width="2"><circle cx="12" cy="12" r="9"/><path d="M3 12h18M12 3c3 3 3 15 0 18M12 3c-3 3-3 15 0 18"/></svg>
        bashbythecreekzq.example
      </div>
    </div>

    <ul class="services">
      <li><svg viewBox="0 0 24 24"><path d="M3 13l6 6L21 5" fill="none" stroke="#f06d92" stroke-width="4" stroke-linecap="round" stroke-linejoin="round"/></svg>Ballons</li>
      <li><svg viewBox="0 0 24 24"><path d="M3 13l6 6L21 5" fill="none" stroke="#f06d92" stroke-width="4" stroke-linecap="round" stroke-linejoin="round"/></svg>Backdrops</li>
      <li><svg viewBox="0 0 24 24"><path d="M3 13l6 6L21 5" fill="none" stroke="#f06d92" stroke-width="4" stroke-linecap="round" stroke-linejoin="round"/></svg>Custom Party Decor</li>
      <li><svg viewBox="0 0 24 24"><path d="M3 13l6 6L21 5" fill="none" stroke="#f06d92" stroke-width="4" stroke-linecap="round" stroke-linejoin="round"/></svg>Full Party Planning</li>
    </ul>
  </main>
</body>
</html>
```